Brindlemark Services Ltd

I'd like to create a company letterhead for the attached logo in word format.

I'd like to emphasis the icon in large translucent state from the left corner and ensure that the letterhead colouring matches the colour palette of the current logo with a contrast so it's clear to see. I've attached a copy of our sister company page on the app for reference.

```html
<!DOCTYPE html>
<html lang="en">
<head>
<meta charset="utf-8">
<title>Brindlemark Services Ltd — Letterhead</title>
<link rel="stylesheet" href="https://fonts.googleapis.com/css2?family=Arimo:wght@400;700&family=Mulish:wght@700;800&family=Roboto+Condensed:wght@300&display=swap">
<style>
  :root {
    --teal: #00bfa6;
    --teal-faint: #eef8f8;
    --grey-band: #9a9a9a;
    --ink: #555555;
    --ink-light: #8e8e8e;
    --rule: #c4c4c4;
    --backdrop: #f2f2f2;
    --paper: #ffffff;
  }
  * { box-sizing: border-box; margin: 0; padding: 0; }
  html, body { width: 1200px; height: 1200px; overflow: hidden; }
  body { background: var(--backdrop); position: relative; font-family: "Arimo", Arial, sans-serif; color: var(--ink); }

  .letterhead {
    position: absolute; left: 233px; top: 81px;
    width: 734px; height: 1038px;
    background: var(--paper);
    overflow: hidden;
  }
  .backdrop-circle {
    position: absolute; left: 128px; top: 283px;
    width: 472px; height: 472px; border-radius: 50%;
    background: var(--teal-faint);
  }
  .brand {
    position: absolute; left: 65px; top: 57px;
    display: flex; align-items: center; gap: 10px;
  }
  .brand-dot { width: 40px; height: 40px; border-radius: 50%; background: var(--teal); }
  .brand-name { font-size: 22px; font-weight: 400; color: var(--teal); letter-spacing: 0.2px; }

  .contact {
    position: absolute; left: 537px; top: 35px;
    font-size: 11.5px; line-height: 13.5px; color: var(--ink-light);
  }
  .contact-address { margin-bottom: 10px; }
  .contact-line { display: flex; align-items: center; gap: 6px; height: 16.5px; }
  .contact-line svg { width: 10px; height: 10px; flex: none; }

  .header-rule {
    position: absolute; left: 65px; top: 130px;
    width: 604px; height: 1px; background: var(--rule);
  }

  .letter-body { position: absolute; left: 65px; top: 319px; width: 605px; }
  .salutation {
    font-family: "Mulish", "Century Gothic", sans-serif; font-weight: 800;
    font-size: 17px; color: var(--ink); margin-left: 2px; margin-bottom: 26px;
  }
  .letter-body p {
    font-size: 12.1px; line-height: 15px; text-align: justify; margin-bottom: 13.5px;
  }
  .sign-off {
    font-family: "Mulish", "Century Gothic", sans-serif; font-weight: 800;
    font-size: 10px; margin: 26px 0 0 2px;
  }
  .signature {
    font-family: "Roboto Condensed", sans-serif; font-weight: 300;
    font-size: 19px; letter-spacing: -0.8px; color: var(--ink);
    margin: 30px 0 0 20px;
  }

  .footer-band { position: absolute; left: 0; bottom: 0; width: 734px; height: 16px; }
</style>
</head>
<body>
  <main class="letterhead">
    <div class="backdrop-circle" aria-hidden="true"></div>

    <div class="brand">
      <span class="brand-dot" aria-hidden="true"></span>
      <span class="brand-name">Brindlemark Services Ltd</span>
    </div>

    <address class="contact" style="font-style:normal">
      <div class="contact-address">Your address, city<br>state, ZIP 0000</div>
      <div class="contact-line">
        <svg viewBox="0 0 10 10" aria-hidden="true"><path fill="var(--teal)" d="M2 0.5 3.6 2.6 2.7 3.6c.6 1.5 1.9 2.8 3.4 3.4l1-.9L9.5 7.8 8.4 9.4C4.3 9.2.8 5.7.6 1.6z"/></svg>
        <span>555-014-2100</span>
      </div>
      <div class="contact-line">
        <svg viewBox="0 0 10 10" aria-hidden="true"><rect x="0.5" y="2" width="9" height="6.5" fill="var(--teal)"/><path d="M0.8 2.3 5 5.6 9.2 2.3" stroke="#fff" stroke-width="0.9" fill="none"/></svg>
        <span>hello@brindlemark.co</span>
      </div>
      <div class="contact-line">
        <svg viewBox="0 0 10 10" aria-hidden="true"><circle cx="5" cy="5" r="4.5" fill="var(--teal)"/><path d="M2.5 3.2h2l.5 1.5-1.5.8.5 2M6.5 2l-.5 1.5 1.8.7" stroke="#fff" stroke-width="0.8" fill="none"/></svg>
        <span>www.brindlemark.co</span>
      </div>
    </address>

    <div class="header-rule" aria-hidden="true"></div>

    <section class="letter-body">
      <h1 class="salutation">Dear Mr. Ashford,</h1>
      <p>Lorem ipsum dolor sit amet, consectetuer adipiscing elit, sed diam nonmmy nibh euismod tincidunt ut laor eet dolore magna aliquam erat volutpat. Ut wisi enim ad minim veniam, quis nostrud exerci tationmcorper suscipit lobortis nisl ut aliquip ex ea commodo consequat. Duis autem vel eum iriure dolor in hendrerit in vulputate velit esse molestie consequat, vel illum dolore eu feugiat</p>
      <p>Rorem ipsum dolor sit amet, consectetuer adipiscing elit, sed diam nonmmy nibh euismod tincidunt ut laor eet dolore magna aliquam erat volutpat. Ut wisi enim ad minim veniam, quis nostrud exerci tationmcorper suscipit lobortis nisl ut aliquip ex ea commodo consequat. Duis autem vel eum iriure dolor in hendrerit in vulputate velit esse molest</p>
      <p>Dorem ipsum dolor sit amet, consectetuer adipiscing elit, sed diam nonmmy nibh euismod tincidunt ut laor eet dolore magna aliquam erat volutpat. Ut wisi enim ad minim veniam, quis nostrud exerci tationmcorper suscipit lobortis nisl ut aliquip ex ea commodo consequat. Duis autem vel eum iriure dolor in hendrerit in suscipit lobortis nisl ut aliquip ex ea commodo consequat. Duis autem vel eum iriure dolor in hendrerit in vulputate velit esse molestie consequat, vel illum</p>
      <p>Sorem ipsum dolor sit amet, consectetuer adipiscing elit, sed diam nonmmy nibh euismod tincidunt ut laor eet dolore magna aliquam erat volutpat. Ut wisi enim ad minim veniam, quis nostrud exerci tationmcorper suscipit lobortis nisl ut aliquip ex ea commodo consequat. Duis autem vel eum iriure dolor in</p>
      <div class="sign-off">Sincerely,</div>
      <div class="signature">Corwin Haldane</div>
    </section>

    <svg class="footer-band" viewBox="0 0 734 16" preserveAspectRatio="none" aria-hidden="true">
      <polygon points="0,0 527,0 514,16 0,16" fill="var(--teal)"/>
      <polygon points="540,0 734,0 734,16 527,16" fill="var(--grey-band)"/>
    </svg>
  </main>
</body>
</html>
```